Renewed Website Design for B2B Company

We need a renewed design for Van Hoorst - an international trading company in raw materials: natural oils (essential oils, fatty oils, and extracts) and related products such as aromas, fragrances, etc.

Page designs to create:

1. Home page (see the mockup, the content and structure should be exactly like this, however feel free creative-wise)

2. Products page(includes all the 11 product categories which you see on van-hoorst.nl and some small description of them).

Current website: van-hoorst.nl
Competitors' websites: brivaroilworks.com & kelmtrade.com (they don't have particularly perfect websites design-wise, however, it's mostly to give you the idea of this market).

Please, go to this Google Drive folder - https://lnk.example/7QpaTzW - to see Van Hoorst's logo in different variations, brandbook with colors, fonts, and a brochure with 'mood board' pictures.

Target Market(s)

B2B companies needing white label products like natural/essential/fatty oils, fragrances etc.

Number of Pages Required

2 page

Font styles to use
Other font styles liked:
• Open Sans

Colors

Designer to choose colors to be used in the design.

Requirements
Should not have
• No images with people; no turqoise, blue or pink colors; no overlays over pictures

```html
<!DOCTYPE html>
<html lang="nl">
<head>
<meta charset="utf-8">
<title>Van Hoorst – Your Reliable Sourcing Partner</title>
<link rel="stylesheet" href="https://fonts.googleapis.com/css2?family=Jost:wght@400;500;600;700&display=swap">
<style>
:root{
  --green:#0c4a1f;
  --green-dark:#083a17;
  --red:#d5001c;
  --grey:#efefef;
  --ink:#2a2a2a;
  --white:#ffffff;
}
*{box-sizing:border-box;margin:0;padding:0}
html,body{width:1200px;height:3839px;overflow:hidden}
body{position:relative;background:var(--white);font-family:'Jost',sans-serif;color:var(--ink)}
.abs{position:absolute}
a{color:inherit;text-decoration:none}

/* hero */
.hero{left:0;top:0;width:1200px;height:708px;background:linear-gradient(180deg,#e4e6ea 0%,#eef0f2 60%,#e2e3e6 100%)}
.hero-photo{left:420px;top:60px;width:660px;height:648px;border-radius:4px;
  background:radial-gradient(ellipse at 30% 65%,#f4b21b 0%,rgba(244,178,27,.4) 18%,transparent 35%),
             radial-gradient(ellipse at 80% 55%,#d9b10e 0%,rgba(217,177,14,.35) 20%,transparent 38%),
             radial-gradient(ellipse at 15% 20%,#e5e27a 0%,transparent 25%),
             linear-gradient(180deg,#e7e8eb,#dcdcdc)}
.brand{left:75px;top:37px;display:flex;align-items:center;gap:14px}
.brand-dot{width:50px;height:50px;border-radius:50%;background:var(--green)}
.brand-name{font-size:44px;font-weight:700;color:var(--red);letter-spacing:.5px;line-height:1}
.nav{top:58px;left:0;width:1200px;font-size:14px;color:#333}
.nav span{position:absolute}
.search{left:1110px;top:60px}
.hero-title{left:134px;top:346px;font-size:35px;font-weight:500;line-height:42px;color:var(--green)}
.btn{display:flex;align-items:center;justify-content:center;border-radius:20px;font-size:13px;color:var(--white)}
.hero-btn{left:134px;top:450px;width:194px;height:38px;background:var(--green);justify-content:flex-start;padding-left:32px;overflow:hidden}
.hero-btn .tip{position:absolute;right:0;top:0;width:60px;height:38px;background:var(--red);border-radius:0 20px 20px 0}
.hero-btn svg{position:absolute;right:12px;top:12px}
.slide-dots{left:30px;top:346px}
.slide-dots i{display:block;width:7px;height:7px;border-radius:50%;background:#9a9a9a;margin-bottom:9px}
.slide-dots i.on{background:var(--green);box-shadow:0 0 0 3px #e4e6ea,0 0 0 4px var(--green)}
.social-rail{left:1149px;top:316px}
.social-rail i{display:block;width:20px;height:20px;border-radius:50%;border:1.5px solid var(--green);margin-bottom:14px}
.social-rail i.red{background:var(--red);border-color:var(--red)}
.notch{left:560px;top:700px;width:80px;height:40px;border-radius:0 0 40px 40px;background:#e2e3e6}

/* products */
.section-title{font-size:33px;font-weight:500;color:var(--green);text-align:center;width:1200px;left:0}
.products-title{top:788px}
.products-sub{top:842px;left:0;width:1200px;text-align:center;font-size:13px;line-height:16px;color:#333}
.switch{top:833px;width:40px;height:40px;border-radius:50%}
.card{top:911px;width:326px;height:441px;background:var(--grey);border-radius:4px;overflow:hidden;text-align:center}
.card-photo{width:326px;height:253px}
.card-icon{position:absolute;left:136px;top:226px;width:54px;height:54px;border-radius:50%;background:var(--white);display:flex;align-items:center;justify-content:center}
.card h3{margin-top:20px;font-size:27px;font-weight:500;color:var(--green)}
.card p{margin:20px auto 0;width:290px;font-size:13px;line-height:15px;color:#444}
.card a{display:inline-block;margin-top:24px;font-size:13px;color:#444;text-decoration:underline}
.cta-green{left:513px;top:1394px;width:182px;height:39px;background:var(--green)}

/* what we do */
.leaves{left:90px;top:1461px;width:1010px;height:156px;border-radius:60px;
  background:linear-gradient(90deg,rgba(122,160,128,.0),#8fb196 15%,#7ea487 50%,#8fb196 85%,rgba(122,160,128,0))}
.band{left:0;top:1585px;width:1200px;height:522px;background:var(--green)}
.leaves-top{left:90px;top:1461px;width:1010px;height:156px;z-index:2;border-radius:70px;opacity:.85;
  background:linear-gradient(90deg,rgba(143,177,150,0),#8fb196 12%,#a4c2a8 50%,#8fb196 88%,rgba(143,177,150,0))}
.wdw-title{top:1698px;color:var(--white)}
.wdw-rule{left:561px;top:1753px;width:78px;height:3px;background:var(--white)}
.wdw-text{left:300px;top:1774px;width:600px;text-align:center;font-size:19px;line-height:22px;color:var(--white);letter-spacing:.3px}
.cta-red{left:513px;top:1898px;width:182px;height:39px;background:var(--red)}
.deco{top:1850px;height:257px}

/* about */
.about-title{left:76px;top:2410px;font-size:33px;font-weight:500;color:var(--green)}
.about-rule{left:76px;top:2464px;width:78px;height:3px;background:var(--green)}
.team-photo{left:402px;top:2224px;width:330px;height:265px;background:linear-gradient(135deg,#e0a24a,#c8413f 45%,#5d7fbf)}
.copy{font-size:14px;line-height:15px;color:#333}
.copy p+p{margin-top:16px}
.about-copy{left:402px;top:2512px;width:315px}
.about-side{left:799px;top:2223px;width:315px}
.emblem{left:832px;top:2340px;width:272px;height:272px;border-radius:50%;background:var(--green);display:flex;align-items:center;justify-content:center;color:var(--white);font-size:36px;font-weight:600}

/* feature */
.feature-photo{left:0;top:2735px;width:714px;height:510px;background:radial-gradient(ellipse at 30% 50%,#d9b44a 0%,#b38a3a 18%,transparent 40%),linear-gradient(180deg,#5b4030,#7a5840 50%,#3d2a1f)}
.hatch{left:733px;top:2838px;width:93px;height:93px;background:#b8b8b8}
.feature-box{left:516px;top:2950px;width:435px;height:377px;background:var(--grey)}
.feature-copy{left:581px;top:3067px;width:320px}

/* footer */
.footer{left:0;top:3245px;width:1200px;height:522px;background:var(--green)}
.footer-brand{left:0;top:3380px;width:1200px;display:flex;justify-content:center;align-items:center;gap:18px}
.footer-brand .dot{width:66px;height:66px;border-radius:50%;background:var(--white)}
.footer-brand span{font-size:56px;font-weight:700;color:var(--white);line-height:1}
.contact{top:3475px;width:300px;text-align:center;color:var(--white);font-size:13px;line-height:15px}
.contact .ico{width:57px;height:57px;border-radius:50%;background:var(--red);margin:0 auto 22px;display:flex;align-items:center;justify-content:center}
.badges{left:486px;top:3628px;display:flex;gap:12px}
.badges i{display:block;width:38px;height:34px;border-radius:17px;background:rgba(255,255,255,.85)}
.footer-rule{left:386px;top:3685px;width:437px;height:1px;background:rgba(255,255,255,.55)}
.footer-nav{top:3708px;left:0;width:1200px;display:flex;justify-content:center;gap:34px;font-size:14px;color:var(--white)}
.bottom{left:0;top:3767px;width:1200px;height:72px;background:var(--white)}
.copyright{left:76px;top:3796px;font-size:12px;color:#333}
.social{top:3785px;width:36px;height:36px;border-radius:50%}
</style>
</head>
<body>

<!-- hero -->
<section class="abs hero">
  <div class="abs hero-photo" role="img" aria-label="Still life with oil jars, a dropper bottle, a glass carafe of golden oil, willow catkins and orange marigolds on a stone"></div>
</section>
<div class="abs notch"></div>
<div class="abs brand"><span class="brand-dot"></span><span class="brand-name">VAN HOORST</span></div>
<nav class="abs nav">
  <span style="left:629px">Producten</span>
  <span style="left:729px">Team</span>
  <span style="left:799px">Werkwijze</span>
  <span style="left:894px">Certificeringen</span>
  <span style="left:1021px">Contact</span>
</nav>
<svg class="abs search" width="16" height="16" viewBox="0 0 16 16"><circle cx="6.5" cy="6.5" r="4.5" fill="none" stroke="#222" stroke-width="1.8"/><line x1="10" y1="10" x2="14.5" y2="14.5" stroke="#222" stroke-width="2"/></svg>
<div class="abs slide-dots"><i></i><i class="on"></i><i></i><i></i></div>
<h1 class="abs hero-title">Your Reliable<br>Sourcing Partner</h1>
<a class="abs btn hero-btn"><span class="tip"></span>Naar Producten<svg width="40" height="14" viewBox="0 0 40 14"><line x1="0" y1="7" x2="37" y2="7" stroke="#fff" stroke-width="2"/><polyline points="31,1 38,7 31,13" fill="none" stroke="#fff" stroke-width="2"/></svg></a>
<div class="abs social-rail"><i></i><i class="red"></i><i></i><i></i></div>

<!-- products -->
<h2 class="abs section-title products-title">Producten</h2>
<p class="abs products-sub">Onze producten zijn onder te verdelen in de volgende productgroepen.<br>Klik op een productgroep voor informatie en het assortiment.</p>
<span class="abs switch" style="left:1034px;background:var(--red)"></span>
<span class="abs switch" style="left:1083px;background:var(--green)"></span>

<article class="abs card" style="left:76px">
  <div class="card-photo" role="img" aria-label="Small corked glass bottles of essential oil with herbs and purple flowers" style="background:linear-gradient(135deg,#d8d2c4,#bfae8a 50%,#c9a6cf)"></div>
  <span class="card-icon"><svg width="26" height="26" viewBox="0 0 26 26"><path d="M13 3c5 5 7 9 7 12a7 7 0 0 1-14 0c0-3 2-7 7-12z" fill="none" stroke="#333" stroke-width="1.6"/></svg></span>
  <h3>Etherische Oliën</h3>
  <p>Van Hoorst is een ervaren leverancier van etherische oliën. Ons belangrijkste kenmerk is de grote diversiteit aan oliën.</p>
  <a>Rood worden</a>
</article>
<article class="abs card" style="left:437px">
  <div class="card-photo" role="img" aria-label="Bottle of fatty oil with walnuts and a cork" style="background:linear-gradient(135deg,#c9a84a,#8a6a45 50%,#c8c2b8)"></div>
  <span class="card-icon"><svg width="26" height="26" viewBox="0 0 26 26"><path d="M13 3c5 5 7 9 7 12a7 7 0 0 1-14 0c0-3 2-7 7-12z" fill="none" stroke="#333" stroke-width="1.6"/></svg></span>
  <h3>Vette Oliën</h3>
  <p>Van Hoorst is een ervaren leverancier van etherische oliën. Ons belangrijkste kenmerk is de grote diversiteit aan oliën.</p>
  <a>Rood worden</a>
</article>
<article class="abs card" style="left:797px">
  <div class="card-photo" role="img" aria-label="Sunflower, sunflower seeds in a burlap sack and a glass carafe of oil" style="background:linear-gradient(135deg,#e4b020,#6b5a3e 45%,#3a3530)"></div>
  <span class="card-icon"><svg width="26" height="26" viewBox="0 0 26 26"><path d="M13 3c5 5 7 9 7 12a7 7 0 0 1-14 0c0-3 2-7 7-12z" fill="none" stroke="#333" stroke-width="1.6"/></svg></span>
  <h3>Extracten</h3>
  <p>Van Hoorst is een ervaren leverancier van etherische oliën. Ons belangrijkste kenmerk is de grote diversiteit aan oliën.</p>
  <a>Rood worden</a>
</article>
<a class="abs btn cta-green">Naar Producten</a>

<!-- what we do -->
<section class="abs band"></section>
<div class="abs leaves-top" role="img" aria-label="Garland of eucalyptus leaves with small yellow blossoms"></div>
<h2 class="abs section-title wdw-title">Wat Doen We?</h2>
<div class="abs wdw-rule"></div>
<p class="abs wdw-text">Van Hoorst is een solide en betrouwbare leverancier van grondstoffen voor de cosmetische-, chemische, reform-, feed- en foodsector. Wij onderscheiden ons door een hoog serviceniveau en uitgebreid aanbod.</p>
<a class="abs btn cta-red">Naar Producten</a>
<div class="abs deco" role="img" aria-label="Rosemary, cinnamon sticks and an amber dropper bottle" style="left:0;width:360px;background:linear-gradient(90deg,rgba(150,170,120,.6),rgba(140,80,40,.5) 50%,rgba(12,74,31,0))"></div>
<div class="abs deco" role="img" aria-label="Bowl of golden oil with marigold flowers" style="left:350px;width:500px;background:radial-gradient(ellipse at 50% 100%,#e8c040 0%,rgba(232,192,64,.5) 30%,rgba(12,74,31,0) 60%)"></div>
<div class="abs deco" role="img" aria-label="Amber dropper bottle and sprigs of lavender" style="left:840px;width:360px;background:linear-gradient(270deg,rgba(120,100,170,.7),rgba(140,80,40,.45) 55%,rgba(12,74,31,0))"></div>

<!-- about -->
<h2 class="abs about-title">Over Ons</h2>
<div class="abs about-rule"></div>
<div class="abs team-photo" role="img" aria-label="Grid of team portraits on colourful backgrounds"></div>
<div class="abs copy about-copy">
  <p>Lorem Ipsum is gewoon een proeftekst van de drukkerij- en zetindustrie. Lorem Ipsum is de standaard proeftekst in de branche sinds de 16e eeuw, toen een onbekende drukker een galei met letters nam en deze door elkaar husselde om een letterboek te maken.</p>
  <p>Het heeft niet alleen vijf eeuwen overleefd, maar ook de sprong naar het elektronische zetwerk en is in wezen onveranderd gebleven.</p>
</div>
<div class="abs copy about-side"><p>Lorem Ipsum is gewoon een proeftekst van de drukkerij- en zetindustrie. Lorem Ipsum is de standaard proeftekst in de branche sinds de 16e eeuw, toen een onbekende drukker een galei met letters nam en deze door elkaar husselde om een letterboek te maken.</p></div>
<div class="abs emblem">Van Hoorst</div>

<!-- feature -->
<div class="abs feature-photo" role="img" aria-label="Glass carafe of coconut oil with coconut pieces and leaves on a wooden table"></div>
<div class="abs hatch"></div>
<div class="abs feature-box"></div>
<div class="abs copy feature-copy">
  <p>Lorem Ipsum is gewoon een proeftekst van de drukkerij- en zetindustrie. Lorem Ipsum is de standaard proeftekst in de branche sinds de 16e eeuw, toen een onbekende drukker een galei met letters nam en deze door elkaar husselde om een letterboek te maken.</p>
  <p>Het heeft niet alleen vijf eeuwen overleefd, maar ook de sprong naar het elektronische zetwerk en is in wezen onveranderd gebleven.</p>
</div>

<!-- footer -->
<footer class="abs footer"></footer>
<div class="abs footer-brand"><span class="dot"></span><span>VAN HOORST</span></div>
<div class="abs contact" style="left:214px">
  <div class="ico"><svg width="24" height="24" viewBox="0 0 24 24"><path d="M6 3l3 0 2 5-2.5 1.5a11 11 0 0 0 6 6L16 13l5 2v3a2 2 0 0 1-2 2A16 16 0 0 1 4 5a2 2 0 0 1 2-2z" fill="#fff"/></svg></div>
  +31 (0)40-2718846
</div>
<div class="abs contact" style="left:452px">
  <div class="ico"><svg width="22" height="26" viewBox="0 0 22 26"><path d="M11 1a9 9 0 0 1 9 9c0 6-9 15-9 15S2 16 2 10a9 9 0 0 1 9-9z" fill="#fff"/><circle cx="11" cy="10" r="3.5" fill="var(--red)"/></svg></div>
  Lindenlaan 22<br>5911 KP Marveld (Noord 318)<br>The Netherlands
</div>
<div class="abs contact" style="left:712px">
  <div class="ico"><svg width="24" height="18" viewBox="0 0 24 18"><rect x="1" y="1" width="22" height="16" rx="2" fill="#fff"/><polyline points="2,2 12,10 22,2" fill="none" stroke="var(--red)" stroke-width="1.8"/></svg></div>
  hallo@van-hoorst.nl
</div>
<div class="abs badges"><i></i><i></i><i></i><i></i><i></i></div>
<div class="abs footer-rule"></div>
<nav class="abs footer-nav"><span>Producten</span><span>Team</span><span>Werkwijze</span><span>Certificeringen</span><span>Contact</span></nav>

<div class="abs bottom"></div>
<p class="abs copyright">Copyright © 2022 <b>VAN HOORST</b>, All Rights Reserved.</p>
<span class="abs social" style="left:945px;background:var(--red)"></span>
<span class="abs social" style="left:994px;background:var(--green)"></span>
<span class="abs social" style="left:1042px;background:var(--green)"></span>
<span class="abs social" style="left:1088px;background:var(--green)"></span>

</body>
</html>
```